Rate sheet redesign

We provide rate sheets to agents for our scenic flights and I would like to make them easier to read and more comprehensive. I'd also like to be able to edit the information in the design, as tours get updated and so do the rates. We've got new product out of shark bay, so the sections would need to be: Perth, Geraldton, Kalbarri and Shark Bay. I've attached what we've been using and also some concept photos.

also a link to our flights online: https://ridgewaterairtours.tavlomo.com/catalog/418352/trips-from-perth

I've put this under brochure redesign as I wasn't sure what a rate sheet would be considered. Open to different formats if it means content is editable.

Need extra days to review

```html
<!DOCTYPE html>
<html lang="en">
<head>
<meta charset="utf-8">
<title>Geraldton Rates – Retail Rates</title>
<link rel="stylesheet" href="https://fonts.googleapis.com/css2?family=Bebas+Neue&family=Montserrat:wght@400;500;600;700;800&display=swap">
<style>
  :root {
    --stage: #474747;
    --paper: #ffffff;
    --orange: #f0992b;
    --blue: #0b4f9c;
    --blue-deep: #0a4488;
    --ink: #1b1b1b;
    --cell: rgba(78, 140, 205, 0.32);
  }
  * { box-sizing: border-box; margin: 0; padding: 0; }
  html, body {
    width: 1200px; height: 903px; overflow: hidden;
    background: var(--stage);
    font-family: "Montserrat", sans-serif;
  }
  .rate-sheet {
    position: absolute; left: 85px; top: 87px;
    width: 1031px; height: 729px;
    background: var(--blue);
    overflow: hidden;
  }
  .sheet-header {
    position: absolute; left: 0; top: 0;
    width: 1031px; height: 209px;
    background: var(--paper);
  }
  .header-stripes { position: absolute; left: 0; top: 0; }
  .brand {
    position: absolute; left: 40px; top: 62px; width: 260px;
    display: flex; flex-direction: column; align-items: center; gap: 10px;
  }
  .brand-dot {
    width: 44px; height: 44px; border-radius: 50%;
    background: var(--blue);
  }
  .brand-name {
    font-weight: 700; font-size: 22px; color: var(--blue);
    text-align: center; line-height: 1.1;
  }
  .sheet-titles {
    position: absolute; right: 48px; top: 34px; text-align: right;
  }
  .sheet-title {
    font-family: "Bebas Neue", sans-serif;
    font-size: 100px; line-height: 1; color: var(--orange);
    letter-spacing: 1px;
  }
  .validity {
    margin-top: 4px;
    font-weight: 700; font-size: 15.5px; color: var(--ink);
  }
  .rate-type {
    margin-top: 6px;
    font-weight: 800; font-size: 30px; color: var(--blue); line-height: 1.1;
  }
  .backdrop {
    position: absolute; left: 0; top: 209px; width: 1031px; height: 520px;
    background: linear-gradient(180deg, #1a5ca8 0%, #2a6db5 40%, #1d5ea9 70%, #0e4f9a 100%);
  }
  .rate-table {
    position: absolute; left: 47px; top: 237px;
    display: grid;
    grid-template-columns: 226px 304px 179px 99px 94px;
    grid-template-rows: 64px 121px 121px 121px;
    column-gap: 8px; row-gap: 6px;
  }
  .col-head {
    background: var(--orange); color: var(--paper);
    font-weight: 700; font-size: 14px;
    display: flex; align-items: center; justify-content: center;
  }
  .rate-table .col-head + .cell, .cell {
    background: var(--cell); color: var(--paper);
    font-size: 11.2px; line-height: 13.3px; text-align: center;
    display: flex; flex-direction: column; align-items: center; justify-content: center;
    padding: 0 12px;
  }
  .cell p + p { margin-top: 13px; }
  .cell.price { font-size: 11.5px; }
</style>
</head>
<body>
  <main class="rate-sheet">
    <div class="backdrop" role="img" aria-label="Airport terminal window view with aircraft on the apron, tinted blue"></div>

    <header class="sheet-header">
      <svg class="header-stripes" width="1031" height="209" viewBox="0 0 1031 209">
        <rect x="0" y="204" width="1031" height="5" fill="var(--orange)"/>
        <polygon points="342,0 373,0 295,209 264,209" fill="var(--orange)"/>
        <polygon points="350,0 364,0 286,209 272,209" fill="var(--blue)"/>
      </svg>
      <div class="brand">
        <div class="brand-dot"></div>
        <div class="brand-name">Ridgewater<br>Air Tours</div>
      </div>
      <div class="sheet-titles">
        <h1 class="sheet-title">GERALDTON RATES</h1>
        <p class="validity">TOUR RATES VALID FROM 1ST APRIL 2025 TO 31ST MARCH 2026</p>
        <p class="rate-type">RETAIL RATES</p>
      </div>
    </header>

    <section class="rate-table">
      <div class="col-head">FLIGHT</div>
      <div class="col-head">INCLUSIONS</div>
      <div class="col-head">CLAUSES</div>
      <div class="col-head">ADULT</div>
      <div class="col-head">CHILD</div>

      <div class="cell"><p>Abrolhos Island Discovery Tour<br>(Flight 303)</p></div>
      <div class="cell">
        <p>Included: Scenic flight from Geraldton to East Wallabi Island return. Morning /Afternoon Tea, and snorkel gear.</p>
        <p>Duration: 1 hour 20 minutes flight time<br>5 hours 30 minutes Total Tour time</p>
      </div>
      <div class="cell"><p>Normal departure time is 8am, however timing is flexible depending on bookings. Start time must be 6 hours before sunset.</p></div>
      <div class="cell price">$550.00</div>
      <div class="cell price">$385.00</div>

      <div class="cell"><p>Abrolhos Island Discovery Tour plus Pink Lake (Flight 304)</p></div>
      <div class="cell">
        <p>Included: Scenic flight from Geraldton to East Wallabi Island return via Pink Lake. Morning /Afternoon Tea, and snorkel gear.</p>
        <p>Duration: 2 hours flight time<br>6 hours Total Tour time</p>
      </div>
      <div class="cell"><p>Normal departure time is 8am, however timing is flexible depending on bookings. Start time must be 6 hours before sunset.</p></div>
      <div class="cell price">$610.00</div>
      <div class="cell price">$427.00</div>

      <div class="cell"><p>Abrolhos Islands and Batavia Shipwreck (Flight 303B)</p></div>
      <div class="cell">
        <p>Included: Scenic flight from Geraldton to East Wallabi Island return, and Morning /Afternoon Tea.</p>
        <p>Duration: 1 hour 20 minutes flight time<br>2 hours Total Tour time</p>
      </div>
      <div class="cell"><p>Normal departure time is 2pm, however timing is flexible depending on bookings. Start time must be 2.5 hours before sunset.</p></div>
      <div class="cell price">$500.00</div>
      <div class="cell price">$350.00</div>
    </section>
  </main>
</body>
</html>
```